Luxury Photoalbum manufacturer needs banner design 8'x8'

We need a banner design for trade show purposes. We supply luxury one-of-a-kind photo albums to boudoir photographers. Our customers are female professional photographers - mostly in the age range of 26 - 40.Design needs to appeal to business women in this age range who see their business help empower women.Follow our website for our current look and feel. www.velvetkeepsake.com
It needs to be 8'x8'

Target Market(s)

Women professional boudoir photographers

Industry/Entity Type

Professional Photography

Font styles to use
Serif

Requirements
Must have
• Feminine but professional look and feel
• Need the LOGO to be very dominant
• Needs to be reasonably consistent with our website - www.velvetkeepsake.com
Nice to have
• Not necessary to use all the images - can use as few or many as makes sense.

```html
<!DOCTYPE html>
<html lang="en">
<head>
<meta charset="utf-8">
<title>Velvet Keepsake – Trade Show Banner</title>
<link rel="stylesheet" href="https://fonts.googleapis.com/css2?family=Playfair+Display:wght@400&display=swap">
<style>
  :root {
    --brand-red: #e41e26;
    --ink-black: #0b0b0b;
    --charcoal: #2b2b2b;
    --ring-grey: #3a3a3a;
    --white: #ffffff;
    --photo-light: #d9d4c9;
    --photo-mid: #b8ad98;
    --photo-dark: #6e665a;
  }
  html, body {
    margin: 0;
    padding: 0;
    width: 1200px;
    height: 1200px;
    overflow: hidden;
    background: var(--ink-black);
  }
  .banner {
    position: relative;
    width: 1200px;
    height: 1200px;
    overflow: hidden;
    background: radial-gradient(circle at 85% 70%, var(--charcoal) 0%, #161616 45%, var(--ink-black) 80%);
    font-family: "Playfair Display", Georgia, serif;
  }
  .banner__art {
    position: absolute;
    inset: 0;
    width: 1200px;
    height: 1200px;
  }
  .brand-name {
    position: absolute;
    left: 560px;
    top: 150px;
    width: 600px;
    margin: 0;
    text-align: center;
    color: var(--brand-red);
    font-weight: 400;
    font-size: 108px;
    line-height: 1.25;
    letter-spacing: 1px;
  }
  .tagline {
    position: absolute;
    left: 477px;
    top: 727px;
    width: 723px;
    height: 263px;
    box-sizing: border-box;
    padding: 38px 0 0 44px;
    margin: 0;
    background: var(--brand-red);
    color: var(--white);
    font-weight: 400;
    font-size: 66px;
    line-height: 1.3;
  }
  .web-address {
    position: absolute;
    left: 0;
    width: 1200px;
    top: 1112px;
    margin: 0;
    text-align: center;
    color: var(--white);
    font-size: 32px;
    letter-spacing: 6px;
  }
</style>
</head>
<body>
  <main class="banner">
    <svg class="banner__art" viewBox="0 0 1200 1200" aria-hidden="false">
      <defs>
        <linearGradient id="portraitTone" x1="0" y1="0" x2="1" y2="1">
          <stop offset="0" stop-color="var(--photo-dark)"/>
          <stop offset="0.35" stop-color="var(--photo-light)"/>
          <stop offset="0.7" stop-color="var(--photo-mid)"/>
          <stop offset="1" stop-color="var(--photo-dark)"/>
        </linearGradient>
      </defs>
      <path class="frame-ring" d="M470 0 C590 200 690 500 672 800 C662 980 648 1100 634 1200"
            fill="none" stroke="var(--ring-grey)" stroke-width="3"/>
      <path class="portrait" role="img"
            aria-label="Boudoir portrait of a woman in black lace lingerie leaning against a wall"
            d="M0 0 H440 C560 200 660 500 640 800 C630 980 615 1100 600 1200 H0 Z"
            fill="url(#portraitTone)"/>
    </svg>

    <h1 class="brand-name">Velvet<br>Keepsake</h1>

    <p class="tagline">Albums that fit<br>your Brand</p>

    <p class="web-address">www.velvetkeepsake.com</p>
  </main>
</body>
</html>
```